Simple, High-Class Web Design Wanted - Motivational Speakers Site

1. Full Brief/Request & Specs outlined on following video -
http://clipvane-recorder.com/watch/tbWrkLmQyP

2. Use colours, images as you feel suits objective (we are happy to pay up to US$30 for any good images but must have licence/permission).

3. Layout probably similar to existing site - www.podiumvoicehub.com.au / http://podiumvoicehub.com.au/contact.php

4. Must Be Able to Coded for MOBILE-FRIENDLINESS & WordPress friendly Ideal.

5. This is the first, small job of many we/graphic design jobs. If suits, winning designer may be offered all future work direct.

Thanks & look forward to your design. Glen.

Target Market(s)

corporates - high end

Number of Pages Required

2 page

Font styles to use
Sans Serif

Requirements
Must have
• Classy professional look
Nice to have
• all in Video in brief
Should not have
• too many images / new images I haven't approved

```html
<!DOCTYPE html>
<html lang="en">
<head>
<meta charset="utf-8">
<title>Podium Voice Hub – Find The Perfect Speaker</title>
<link href="https://fonts.googleapis.com/css2?family=Roboto:wght@300;400;500;700&display=swap" rel="stylesheet">
<style>
  :root{
    --page:#eceef0;
    --hero-top:#5d7186;
    --hero-bottom:#2f4458;
    --ink:#4a4f55;
    --ink-soft:#6b7178;
    --rule:#c9ced3;
    --band:#4ba9de;
    --btn-blue:#3d9fdf;
    --btn-green:#39b58b;
    --footer:#2d3841;
    --footer-ink:#9aa6b0;
    --white:#ffffff;
  }
  *{box-sizing:border-box;margin:0;padding:0}
  html,body{width:730px;height:1200px;overflow:hidden}
  body{background:var(--page);font-family:"Roboto",Arial,sans-serif;color:var(--ink);position:relative}

  .hero{position:absolute;left:0;top:0;width:730px;height:232px;overflow:hidden}
  .hero-photo{position:absolute;inset:0;background:linear-gradient(170deg,var(--hero-top) 0%,#44596d 55%,var(--hero-bottom) 100%)}
  .hero-title{position:absolute;left:112px;top:40px;width:420px;color:var(--white);font-weight:400;font-size:27px;line-height:32px}
  .hero-title span{display:block;font-size:22px;font-weight:300}
  .hero-rule{position:absolute;left:112px;top:108px;width:270px;height:1px;background:rgba(255,255,255,.55)}
  .hero-lead{position:absolute;left:375px;top:112px;width:300px;color:var(--white);font-size:13px;line-height:17px;font-weight:300}
  .hero-contact{position:absolute;left:578px;top:188px;width:76px;height:20px;border:1px solid rgba(255,255,255,.7);color:var(--white);font-size:9px;letter-spacing:1px;line-height:18px;text-align:center;text-transform:uppercase}

  .video{position:absolute;left:182px;top:240px;width:366px;height:212px;background:var(--white);box-shadow:0 2px 6px rgba(0,0,0,.15)}
  .video-still{position:absolute;left:0;top:0;width:366px;height:190px;background:linear-gradient(90deg,#dfe4e8 0%,#c8d2db 50%,#dfe4e8 100%)}
  .video-play{position:absolute;left:160px;top:72px}
  .video-bar{position:absolute;left:0;top:190px;width:366px;height:22px;background:#f5f6f7;border-top:1px solid #e1e4e7}
  .video-bar i{position:absolute;top:6px;width:10px;height:10px;border-radius:50%;border:1px solid #9ba3aa}

  .cta-blue{position:absolute;left:220px;top:468px;width:290px;height:22px;background:var(--btn-blue);color:var(--white);font-size:10px;font-weight:500;line-height:22px;text-align:center;border-radius:2px}

  .section-title{position:absolute;left:0;width:730px;text-align:center;font-weight:300;font-size:20px;color:var(--ink)}
  .section-title::before,.section-title::after{content:"";position:absolute;top:50%;width:225px;height:1px;background:var(--rule)}
  .section-title::before{left:110px}
  .section-title::after{right:110px}
  .copy{position:absolute;left:110px;width:510px;font-size:9.5px;line-height:14px;color:var(--ink-soft)}
  .copy p{margin-bottom:7px}
  .copy.center{text-align:center}

  .band{position:absolute;left:0;top:680px;width:730px;height:150px;background:var(--band);color:var(--white);text-align:center;font-size:9.5px;line-height:13px;padding-top:28px}
  .band p{margin-bottom:13px}
  .band b{font-weight:500}

  .cta-green{position:absolute;height:22px;background:var(--btn-green);color:var(--white);font-size:10px;font-weight:500;letter-spacing:.4px;line-height:22px;text-align:center;border-radius:2px;text-transform:uppercase}

  .contact-line{position:absolute;left:330px;top:1098px;font-size:9.5px;color:var(--ink-soft);line-height:22px}
  .contact-line b{color:var(--btn-green);font-weight:500}

  .footer{position:absolute;left:0;top:1148px;width:730px;height:52px;background:var(--footer);color:var(--footer-ink);font-size:8px;line-height:12px;text-align:center;padding-top:14px}
  .to-top{position:absolute;right:90px;top:14px;width:22px;height:22px;background:#4a5864}
</style>
</head>
<body>

<header class="hero">
  <div class="hero-photo" role="img" aria-label="Conference room with a long table and large windows, tinted blue"></div>
  <h1 class="hero-title">Find The Perfect Speaker For Your Next Event Here <span>- free industry service</span></h1>
  <div class="hero-rule"></div>
  <p class="hero-lead">Looking for a top motivational or guest speaker, MC, industry expert to "WOW" your audience - find them here</p>
  <div class="hero-contact">Contact</div>
</header>

<div class="video">
  <div class="video-still" role="img" aria-label="Introductory video still of the service host speaking to camera"></div>
  <svg class="video-play" width="46" height="46" viewBox="0 0 46 46" aria-hidden="true">
    <circle cx="23" cy="23" r="22" fill="#39b58b" opacity=".9"/>
    <path d="M18 14 L33 23 L18 32 Z" fill="#fff"/>
  </svg>
  <div class="video-bar">
    <i style="left:8px"></i><i style="left:22px"></i><i style="left:36px"></i><i style="right:8px"></i>
  </div>
</div>

<div class="cta-blue">I Want to Make an Event a Great Success &#9656;</div>

<h2 class="section-title" style="top:536px">About</h2>
<div class="copy" style="top:572px">
  <p>Podium Voice Hub is a free industry service designed to help people looking for speakers avoid precious time and frustration in finding the most suitable best speaker for their needs.</p>
  <p>Suggestions are given by Podium Voice Hub conference speaker Glen, who has presented around Australia for a number of years and is familiar with many of our top professional speakers, MCs as well as the leading speaker bureaus.</p>
  <p>If you would like a hand finding some good speaker options, simply send us the details of your event and the type of presenter you are ideally after, e.g.</p>
</div>

<section class="band">
  <p><b>Types/Style</b> – Motivational, Entertaining, Keynote/Workshop, MC etc</p>
  <p><b>Topics/Area</b> – Team Building, Leadership, Business, Health/Life balance etc</p>
  <p><b>Approximate Budget</b> – $1000, $2000, $5000, $7000+ etc</p>
  <p><b>Location</b> – Sydney, Melbourne, Brisbane, Perth, Adelaide, Canberra etc</p>
</section>
<div class="cta-green" style="left:268px;top:818px;width:194px">Complete Online Contact Form &#9656;</div>

<div class="copy" style="top:852px">
  <p>and when we can, we will be happy to send you some speaker possibilities ideas, trusted speakers bureaus or simply some thoughts on the best places for you to look. Regards, Glen.</p>
</div>

<h2 class="section-title" style="top:912px">Note</h2>
<div class="copy center" style="top:956px">
  <p>Any information you provide will ONLY ever be used to help with your specific enquiry.</p>
  <p>Glen does not have any financial agreements with any individual speakers he recommends. He offers this service as it only takes a few minutes of his time, helps promote other professional speakers and obviously keeps his own name out there in the industry.</p>
  <p>Please understand that while Glen tries to respond quickly, due to his own speaking/travel commitments it may take up to 24 hours.</p>
</div>

<div class="cta-green" style="left:110px;top:1098px;width:206px">Complete Online Contact Form &#9656;</div>
<p class="contact-line"><b>EMAIL:</b> suggestions@podiumvoicehub.com.au &nbsp;<b>PHONE:</b> 1300 555 019</p>

<footer class="footer">
  <p>© 2015 All Rights Reserved podiumvoicehub.com.au PO Box 418, Harbourview NSW 2000</p>
  <p>Email: suggestions@podiumvoicehub.com.au Phone: 1300 555 019</p>
  <svg class="to-top" viewBox="0 0 22 22" aria-hidden="true">
    <rect width="22" height="22" fill="#4a5864"/>
    <path d="M6 13 L11 8 L16 13" fill="none" stroke="#fff" stroke-width="2"/>
  </svg>
</footer>

</body>
</html>
```